Business Cards that are elegant and wow

I want to create and print business cards that represent my brand and stand out from the rest. We want to ensure they stay in our branding and the integrity is not lost. I am happy to look at different shapes like square etc.

It will be printed on very thick cards and will be stylish .

I want to create and print business cards that represent my brand and stand out from the rest. We want to ensure they stay in ur branding and the integrity is not lost. I am happy to look at different shapes like square etc.

Target Market(s)

real estate professionals

Industry/Entity Type

Real Estate

Contact Information for Business Card

Wren Holt
hello@bramblecovehomes.com.au
bramblecovehomes.com.au
0417 382 906 (SMS)

Colors

Designer to choose colors to be used in the design.

Requirements
Must have
• My logo
• email
• website
• Name
Nice to have
• I like the idea of printing with foil or spot gloss. You want it to stand out in a sea.
Should not have
• I would like you to stay in my colour themes. Don't change the colour of my logo

```html
<!DOCTYPE html>
<html lang="en">
<head>
<meta charset="utf-8">
<title>Bramble Cove Homes – Business Card</title>
<link rel="stylesheet" href="https://fonts.googleapis.com/css2?family=Lato:wght@400;700&display=swap">
<style>
  :root {
    --page: #eff0f0;
    --card: #ffffff;
    --pink: #ee3768;
    --green: #a3b55f;
    --blue: #0098cc;
    --brand-blue: #1aa9e1;
    --fold: #3a3a3a;
    --white: #ffffff;
  }
  * { margin: 0; padding: 0; box-sizing: border-box; }
  html, body {
    width: 1050px; height: 1200px; overflow: hidden;
    background: var(--page);
    font-family: "Lato", Arial, sans-serif;
  }
  .card {
    position: absolute;
    left: 148px;
    width: 757px;
    height: 434px;
    background: var(--card);
    overflow: hidden;
    box-shadow: 3px 3px 4px rgba(0,0,0,0.35);
  }
  .card--front { top: 86px; }
  .card--back { top: 683px; }
  .card__shapes { position: absolute; inset: 0; width: 757px; height: 434px; }

  .brand {
    position: absolute;
    display: flex;
    align-items: center;
    color: var(--brand-blue);
    font-weight: 700;
    text-transform: uppercase;
    line-height: 1;
  }
  .brand__dot {
    border-radius: 50%;
    background: var(--brand-blue);
    flex: none;
  }
  .card--front .brand { left: 67px; top: 58px; gap: 16px; font-size: 27px; }
  .card--front .brand__dot { width: 62px; height: 62px; }
  .card--back .brand { left: 155px; top: 50px; gap: 22px; font-size: 46px; }
  .card--back .brand__dot { width: 100px; height: 100px; }

  .holder-name {
    position: absolute;
    left: 382px; top: 54px;
    width: 375px; height: 75px;
    display: flex; align-items: center; justify-content: center;
    padding-left: 20px;
    color: var(--white);
    font-size: 44px;
    font-weight: 700;
    text-transform: uppercase;
  }

  .contacts {
    position: absolute;
    left: 25px; top: 298px;
    list-style: none;
    color: var(--white);
    font-size: 17px;
    letter-spacing: 0.3px;
  }
  .contacts li {
    display: flex; align-items: center;
    height: 40px;
  }
  .contacts svg { width: 26px; height: 26px; margin-right: 12px; flex: none; }

  .web-ribbon {
    position: absolute;
    left: 0; top: 285px; width: 757px; height: 82px;
    display: flex; align-items: center; justify-content: center;
    padding-left: 5px;
    color: var(--white);
    font-size: 32px;
    letter-spacing: 5px;
    white-space: nowrap;
  }
</style>
</head>
<body>

<section class="card card--front" aria-label="Business card front">
  <svg class="card__shapes" viewBox="0 0 757 434" aria-hidden="true">
    <rect x="378" y="49" width="379" height="3" fill="var(--blue)"/>
    <rect x="396" y="131" width="361" height="3" fill="var(--blue)"/>
    <polygon points="380,54 757,54 757,129 408,129" fill="var(--pink)"/>
    <line x1="372" y1="32" x2="416" y2="152" stroke="var(--fold)" stroke-width="2"/>
    <polygon points="527,372 642,372 667,434 550,434" fill="var(--blue)"/>
    <polygon points="372,292 492,292 547,434 422,434" fill="var(--green)"/>
    <polygon points="0,252 352,252 419,434 0,434" fill="var(--pink)"/>
    <line x1="356" y1="252" x2="423" y2="434" stroke="var(--fold)" stroke-width="2"/>
    <line x1="496" y1="292" x2="551" y2="434" stroke="var(--fold)" stroke-width="2"/>
    <line x1="645" y1="372" x2="670" y2="434" stroke="var(--fold)" stroke-width="2"/>
  </svg>

  <div class="brand">
    <span class="brand__dot"></span>
    <span>Bramble Cove<br>Homes</span>
  </div>

  <div class="holder-name">Wren Holt</div>

  <ul class="contacts">
    <li>
      <svg viewBox="0 0 26 26" fill="none" stroke="var(--brand-blue)" stroke-width="1.6"><rect x="2" y="6" width="22" height="15"/><path d="M2 6l11 9 11-9M2 21l8-7M24 21l-8-7"/></svg>
      hello@bramblecovehomes.com.au
    </li>
    <li>
      <svg viewBox="0 0 26 26" fill="none" stroke="var(--brand-blue)" stroke-width="1.6"><circle cx="13" cy="13" r="10"/><ellipse cx="13" cy="13" rx="4.5" ry="10"/><path d="M3 13h20M5 8h16M5 18h16"/></svg>
      bramblecovehomes.com.au
    </li>
    <li>
      <svg viewBox="0 0 26 26" fill="none" stroke="var(--brand-blue)" stroke-width="1.6"><rect x="7" y="1" width="12" height="24" rx="2"/><path d="M7 5h12M7 20h12"/><circle cx="13" cy="22.5" r="0.8"/></svg>
      0417 382 906 (SMS)
    </li>
  </ul>
</section>

<section class="card card--back" aria-label="Business card back">
  <svg class="card__shapes" viewBox="0 0 757 434" aria-hidden="true">
    <rect x="0" y="222" width="757" height="6" fill="var(--blue)"/>
    <rect x="0" y="228" width="757" height="206" fill="var(--pink)"/>
    <rect x="0" y="283" width="757" height="86" fill="var(--green)"/>
    <rect x="0" y="286" width="757" height="80" fill="var(--white)"/>
    <polygon points="102,283 655,283 686,369 70,369" fill="var(--pink)"/>
    <line x1="104" y1="262" x2="62" y2="385" stroke="var(--fold)" stroke-width="2"/>
    <line x1="642" y1="262" x2="684" y2="385" stroke="var(--fold)" stroke-width="2"/>
  </svg>

  <div class="brand">
    <span class="brand__dot"></span>
    <span>Bramble Cove<br>Homes</span>
  </div>

  <div class="web-ribbon">bramblecovehomes.com.au</div>
</section>

</body>
</html>
```